Business Card - Professional Minimalist - Double sided

We appreciate minimalist logo/web/collateral designs that allow design to tell a story. We want to relay a professional image/approach but throwing in a splash of modern when we’re able so long as it’s not distracting. Think 75% classic corporate, 25% modern. Open to black or white design, not sure which might look the best.

Target Market(s)

Senior executives or related government affairs contacts within the agriculture, energy, and defense industries (i.e., potential clients) but located outside of Washington, DC. Most potential clients based in DC with be familiar with both of us and our shared history.

Industry/Entity Type

Consulting

Contact Information for Business Card

Name: Daniel R. Whitlock
Title: Co-Founder & Partner
Address: 418 Bramblewood Ave. SE | Suite 2716 | Washington, D.C. 20019
Phone: (202) 555-0187
Email: Daniel@HollerbyWhitlock.com

Font styles to use
Serif

Colors

Designer to choose only greyscale colors for use in the design.

Requirements
Must have
• Name: Daniel R. Whitlock
Phone: (202) 555-0187

```html
<!DOCTYPE html>
<html lang="en">
<head>
<meta charset="utf-8">
<title>Hollerby Whitlock Group — Business Card</title>
<link href="https://fonts.googleapis.com/css2?family=Libre+Baskerville:wght@400;700&display=swap" rel="stylesheet">
<style>
  :root {
    --page-bg: #f1f1f1;
    --card-bg: #ffffff;
    --card-edge: #d6d6d6;
    --ink-strong: #2b2b2b;
    --ink: #3a3a3a;
    --ink-mark: #5a5a5a;
    --rule: #bdbdbd;
  }
  * { margin: 0; padding: 0; box-sizing: border-box; }
  html, body {
    width: 1084px;
    height: 1200px;
    overflow: hidden;
    background: var(--page-bg);
    font-family: "Libre Baskerville", Georgia, serif;
    color: var(--ink);
  }
  .canvas { position: relative; width: 1084px; height: 1200px; }
  .card {
    position: absolute;
    width: 487px;
    height: 316px;
    background: var(--card-bg);
    border: 1px solid var(--card-edge);
  }
  .card--front { left: 135px; top: 240px; }
  .card--back { left: 435px; top: 603px; }

  .brand {
    position: absolute;
    left: 0; right: 0; top: 146px;
    display: flex;
    align-items: center;
    justify-content: center;
    gap: 10px;
  }
  .brand__square {
    width: 22px; height: 22px;
    background: var(--ink-mark);
  }
  .brand__name {
    font-size: 16px;
    font-weight: 400;
    letter-spacing: 1.5px;
    text-transform: uppercase;
    color: var(--ink-mark);
  }

  .holder {
    position: absolute;
    left: 0; right: 0; top: 106px;
    text-align: center;
  }
  .holder__name {
    font-size: 17px;
    font-weight: 700;
    color: var(--ink-strong);
    letter-spacing: 0.3px;
  }
  .holder__title-row {
    margin-top: 6px;
    display: flex;
    align-items: center;
    justify-content: center;
    gap: 10px;
  }
  .holder__rule { width: 94px; height: 1px; background: var(--rule); }
  .holder__title { font-size: 12.5px; color: var(--ink); }

  .contact {
    position: absolute;
    left: 0; right: 0; top: 242px;
    text-align: center;
    font-size: 11px;
    line-height: 16px;
    color: var(--ink);
  }
  .contact__address { margin-top: 5px; font-size: 10.5px; }
</style>
</head>
<body>
<div class="canvas">
  <section class="card card--front" aria-label="Card front">
    <div class="brand">
      <span class="brand__square"></span>
      <span class="brand__name">Hollerby Whitlock Group</span>
    </div>
  </section>

  <section class="card card--back" aria-label="Card back">
    <div class="holder">
      <h1 class="holder__name">Daniel R. Whitlock</h1>
      <div class="holder__title-row">
        <span class="holder__rule"></span>
        <span class="holder__title">Co-Founder &amp; Partner</span>
        <span class="holder__rule"></span>
      </div>
    </div>
    <div class="contact">
      <p class="contact__phone">(202) 555-0187</p>
      <p class="contact__email">Daniel@HollerbyWhitlock.com</p>
      <p class="contact__address">418 Bramblewood Ave. SE | Suite 2716 | Washington, D.C. 20019</p>
    </div>
  </section>
</div>
</body>
</html>
```